Real Estate Company / Capital Needs Cards!

need business cards designed using the logos that were just designed by sketchhive.

Reason: per designers request deadline extended 1 day…thank you.

Target Market(s)

Investors and clients looking to purchase real estate or invest in the business.

Industry/Entity Type

Business

Requirements
Must have
• two designs - one for the real estate logo and one for the capital logo, similar but slightly different.
Nice to have
• something to make it pop (perhaps on the back)
Should not have
• much color

```html
<!DOCTYPE html>
<html lang="en">
<head>
<meta charset="utf-8">
<title>Maren Real Estate – Business Cards</title>
<link href="https://fonts.googleapis.com/css2?family=Cinzel:wght@400&family=Open+Sans:wght@400;600&display=swap" rel="stylesheet">
<style>
  :root {
    --page-bg: #e9e9ec;
    --card-white: #f7f7f5;
    --card-black: #141414;
    --gold: #dccf9f;
    --ink: #2a2a2a;
    --ink-soft: #555555;
    --rule: #9a9a9a;
  }
  * { margin: 0; padding: 0; box-sizing: border-box; }
  html, body {
    width: 1200px;
    height: 864px;
    overflow: hidden;
    background: var(--page-bg);
  }
  .canvas {
    position: relative;
    width: 1200px;
    height: 864px;
    display: flex;
    flex-direction: column;
    align-items: center;
    justify-content: center;
    gap: 44px;
  }
  .card {
    width: 640px;
    height: 366px;
    border-radius: 4px;
    box-shadow: 0 6px 18px rgba(0,0,0,0.18);
    position: relative;
    overflow: hidden;
  }

  /* Back: contact side */
  .card-back {
    background: var(--card-white);
  }
  .back-identity {
    position: absolute;
    right: 340px;
    top: 132px;
    text-align: right;
    font-family: "Open Sans", sans-serif;
    color: var(--ink);
  }
  .person-name {
    font-size: 26px;
    font-weight: 600;
    letter-spacing: 0.5px;
    line-height: 1.1;
  }
  .person-role {
    font-size: 15px;
    color: var(--ink-soft);
  }
  .back-divider {
    position: absolute;
    left: 318px;
    top: 120px;
    width: 1px;
    height: 140px;
    background: var(--rule);
  }
  .contact-list {
    position: absolute;
    left: 334px;
    top: 150px;
    list-style: none;
    font-family: "Open Sans", sans-serif;
    font-size: 14px;
    color: var(--ink);
  }
  .contact-item {
    display: flex;
    align-items: center;
    gap: 12px;
    height: 26px;
  }
  .contact-icon {
    width: 16px;
    height: 16px;
    flex: none;
    fill: var(--ink);
  }

  /* Front: brand side */
  .card-front {
    background: var(--card-black);
    display: flex;
    align-items: center;
    justify-content: center;
    gap: 22px;
  }
  .brand-mark {
    width: 96px;
    height: 96px;
    background: var(--gold);
    border-radius: 6px;
    flex: none;
  }
  .brand-name {
    font-family: "Cinzel", serif;
    font-weight: 400;
    color: var(--gold);
    line-height: 1;
  }
  .brand-name-main {
    display: block;
    font-size: 62px;
    letter-spacing: 2px;
  }
  .brand-name-sub {
    display: block;
    font-size: 24px;
    letter-spacing: 5px;
    margin-top: 6px;
  }
</style>
</head>
<body>
<main class="canvas">

  <section class="card card-back" aria-label="Card back with contact details">
    <div class="back-identity">
      <p class="person-name">YOUR NAME</p>
      <p class="person-role">Web Designer</p>
    </div>
    <div class="back-divider"></div>
    <ul class="contact-list">
      <li class="contact-item">
        <svg class="contact-icon" viewBox="0 0 16 16"><rect x="1" y="3" width="14" height="10" rx="1"/><path d="M1.5 3.5 8 9l6.5-5.5" fill="none" stroke="#f7f7f5" stroke-width="1.4"/></svg>
        <span>hello@marenestate.com</span>
      </li>
      <li class="contact-item">
        <svg class="contact-icon" viewBox="0 0 16 16"><path d="M4 1h8a1 1 0 0 1 1 1v12a1 1 0 0 1-1 1H4a1 1 0 0 1-1-1V2a1 1 0 0 1 1-1zm1 2v9h6V3z"/></svg>
        <span>014 382 5170</span>
      </li>
      <li class="contact-item">
        <svg class="contact-icon" viewBox="0 0 16 16"><circle cx="8" cy="8" r="7" fill="none" stroke="#2a2a2a" stroke-width="1.6"/><path d="M1 8h14M8 1c3 3 3 11 0 14M8 1c-3 3-3 11 0 14" fill="none" stroke="#2a2a2a" stroke-width="1.2"/></svg>
        <span>www.marenestate.com</span>
      </li>
      <li class="contact-item">
        <svg class="contact-icon" viewBox="0 0 16 16"><path d="M8 1a5 5 0 0 1 5 5c0 4-5 9-5 9S3 10 3 6a5 5 0 0 1 5-5zm0 3a2 2 0 1 0 0 4 2 2 0 0 0 0-4z"/></svg>
        <span>12 Harbor Road</span>
      </li>
    </ul>
  </section>

  <section class="card card-front" aria-label="Card front with company name">
    <div class="brand-mark"></div>
    <h1 class="brand-name">
      <span class="brand-name-main">MAREN</span>
      <span class="brand-name-sub">REAL ESTATE</span>
    </h1>
  </section>

</main>
</body>
</html>
```